依頼詳細
会社のカラーは
http://kinotesu-sample.com/

サイズは、名刺サイズでお願いします。
記載項目
●賞状のタイトル

こもれび月間AWARD
「成長」部門
「おもいやり」部門
「プロフェッショナル」部門
「最多投票」部門
※それぞれ

●受賞者の名前 フルネーム
●対象月:2016年4月

●文章:
あなたは、こもれびAWARD「●●部門」において、
もっとも多くの成果をあげ、当社の成長と発展に多大なる貢献をされました。
よってここにその功績を高く賞賛し表彰いたします。

株式会社こもれび
委員長 ●●●●
希望イメージ
シンプル 複雑
単色 カラフル
暗い 明るい
日常 高級
遊び心 厳粛
未来的 伝統的
女性的 男性的
希望する色
青系、水色系
納品ファイル
• 高解像度JPG (.jpg)
• イラストレーター形式 (.ai)
■ 選んだ理由

シンプルでうちの雰囲気に合ってるきがしました。
もらって集めてもうれしいカードになるかなと思いました。

■ 提案者全員のお礼・コメント

短い期間でしたが、たくさん応募いただきましてありがとうございます。

```html
<!DOCTYPE html>
<html lang="ja">
<head>
<meta charset="utf-8">
<title>こもれび月間AWARD 表彰カード</title>
<link href="https://fonts.googleapis.com/css2?family=Noto+Sans+JP:wght@400;500;700&family=M+PLUS+Rounded+1c:wght@800&display=swap" rel="stylesheet">
<style>
  :root {
    --brand-blue: #1a9de0;
    --brand-blue-dark: #1487c6;
    --brand-blue-light: #4cb4ea;
    --ribbon-fold: #0f6fa8;
    --ink: #111111;
    --white: #ffffff;
    --growth: #2f9a3a;
    --kindness: #e0262a;
    --professional: #1f7fd0;
    --votes: #e8741a;
  }
  * { margin: 0; padding: 0; box-sizing: border-box; }
  html, body {
    width: 1200px; height: 3096px; overflow: hidden;
    background: var(--white);
  }
  body {
    font-family: "Noto Sans JP", sans-serif;
    color: var(--ink);
    display: flex; flex-direction: column; gap: 72px;
  }
  .award-card {
    position: relative; width: 1200px; height: 720px;
    background: var(--white); overflow: hidden;
  }
  .ribbon { position: absolute; left: 0; top: 0; width: 800px; height: 150px; }
  .ribbon-title {
    position: absolute; left: 72px; top: 26px;
    font-family: "M PLUS Rounded 1c", sans-serif; font-weight: 800;
    font-size: 58px; color: var(--white); letter-spacing: 1px;
    transform: rotate(-4deg); transform-origin: left center;
    white-space: nowrap;
  }
  .brand {
    position: absolute; right: 44px; top: 36px;
    display: flex; align-items: center; gap: 16px;
  }
  .brand-mark { width: 54px; height: 54px; border-radius: 50%; background: var(--brand-blue); }
  .brand-name { font-size: 52px; font-weight: 700; color: var(--brand-blue); }
  .category {
    position: absolute; left: 182px; top: 150px;
    font-size: 50px; font-weight: 700; letter-spacing: 1px;
  }
  .category.growth { color: var(--growth); }
  .category.kindness { color: var(--kindness); }
  .category.professional { color: var(--professional); }
  .category.votes { color: var(--votes); }
  .recipient {
    position: absolute; left: 0; right: 0; top: 220px;
    text-align: center; padding-left: 130px;
    font-size: 84px; font-weight: 700; letter-spacing: 4px;
  }
  .honorific { font-size: 52px; letter-spacing: 0; }
  .rule {
    position: absolute; left: 180px; right: 40px; top: 322px;
    height: 4px; background: var(--brand-blue);
  }
  .award-month {
    position: absolute; right: 72px; top: 334px;
    font-size: 36px; font-weight: 400;
  }
  .citation-panel {
    position: absolute; left: 0; right: 0; top: 388px; bottom: 0;
    background: linear-gradient(to bottom, var(--brand-blue) 0%, var(--brand-blue) 86%, var(--brand-blue-light) 86%);
    color: var(--white);
  }
  .citation {
    position: absolute; left: 40px; top: 18px;
    font-size: 29px; line-height: 48px; font-weight: 400;
  }
  .signature {
    position: absolute; left: 860px; top: 168px;
    font-size: 31px; line-height: 56px; font-weight: 500;
  }
  .signature .dots { margin-left: 22px; letter-spacing: 2px; }
</style>
</head>
<body>

<section class="award-card">
  <svg class="ribbon" viewBox="0 0 800 150" aria-hidden="true">
    <polygon points="0,56 40,40 40,118 0,132" fill="var(--ribbon-fold)"/>
    <polygon points="30,30 780,0 760,60 780,96 36,128" fill="var(--brand-blue)"/>
  </svg>
  <div class="ribbon-title">こもれび月間AWARD</div>
  <div class="brand"><span class="brand-mark"></span><span class="brand-name">こもれび</span></div>
  <div class="category growth">「成長」部門</div>
  <div class="recipient">青木健太<span class="honorific">殿</span></div>
  <div class="rule"></div>
  <div class="award-month">2016年4月</div>
  <div class="citation-panel">
    <p class="citation">あなたは、こもれびAWARD「成長部門」において、<br>もっとも多くの成果をあげ、当社の成長と発展に多大なる貢献をされました。<br>よってここにその功績を高く賞賛し表彰いたします。</p>
    <p class="signature">株式会社こもれび<br>委員長<span class="dots">●●●●</span></p>
  </div>
</section>

<section class="award-card">
  <svg class="ribbon" viewBox="0 0 800 150" aria-hidden="true">
    <polygon points="0,56 40,40 40,118 0,132" fill="var(--ribbon-fold)"/>
    <polygon points="30,30 780,0 760,60 780,96 36,128" fill="var(--brand-blue)"/>
  </svg>
  <div class="ribbon-title">こもれび月間AWARD</div>
  <div class="brand"><span class="brand-mark"></span><span class="brand-name">こもれび</span></div>
  <div class="category kindness">「おもいやり」部門</div>
  <div class="recipient">青木健太<span class="honorific">殿</span></div>
  <div class="rule"></div>
  <div class="award-month">2016年4月</div>
  <div class="citation-panel">
    <p class="citation">あなたは、こもれびAWARD「おもいやり部門」において、<br>もっとも多くの成果をあげ、当社の成長と発展に多大なる貢献をされました。<br>よってここにその功績を高く賞賛し表彰いたします。</p>
    <p class="signature">株式会社こもれび<br>委員長<span class="dots">●●●●</span></p>
  </div>
</section>

<section class="award-card">
  <svg class="ribbon" viewBox="0 0 800 150" aria-hidden="true">
    <polygon points="0,56 40,40 40,118 0,132" fill="var(--ribbon-fold)"/>
    <polygon points="30,30 780,0 760,60 780,96 36,128" fill="var(--brand-blue)"/>
  </svg>
  <div class="ribbon-title">こもれび月間AWARD</div>
  <div class="brand"><span class="brand-mark"></span><span class="brand-name">こもれび</span></div>
  <div class="category professional">「プロフェッショナル」部門</div>
  <div class="recipient">青木健太<span class="honorific">殿</span></div>
  <div class="rule"></div>
  <div class="award-month">2016年4月</div>
  <div class="citation-panel">
    <p class="citation">あなたは、こもれびAWARD「プロフェッショナル部門」において、<br>もっとも多くの成果をあげ、当社の成長と発展に多大なる貢献をされました。<br>よってここにその功績を高く賞賛し表彰いたします。</p>
    <p class="signature">株式会社こもれび<br>委員長<span class="dots">●●●●</span></p>
  </div>
</section>

<section class="award-card">
  <svg class="ribbon" viewBox="0 0 800 150" aria-hidden="true">
    <polygon points="0,56 40,40 40,118 0,132" fill="var(--ribbon-fold)"/>
    <polygon points="30,30 780,0 760,60 780,96 36,128" fill="var(--brand-blue)"/>
  </svg>
  <div class="ribbon-title">こもれび月間AWARD</div>
  <div class="brand"><span class="brand-mark"></span><span class="brand-name">こもれび</span></div>
  <div class="category votes">「最多投票」部門</div>
  <div class="recipient">青木健太<span class="honorific">殿</span></div>
  <div class="rule"></div>
  <div class="award-month">2016年4月</div>
  <div class="citation-panel">
    <p class="citation">あなたは、こもれびAWARD「最多投票部門」において、<br>もっとも多くの成果をあげ、当社の成長と発展に多大なる貢献をされました。<br>よってここにその功績を高く賞賛し表彰いたします。</p>
    <p class="signature">株式会社こもれび<br>委員長<span class="dots">●●●●</span></p>
  </div>
</section>

</body>
</html>
```